Graphic to show our studio's values

We'd like to create a graphic of our values that can go onto fun gifts for our team in order to keep our values in front of all of us in a creative way. The graphic might go onto mugs, gift boxes, tote bags, etc. We are a growing interior architecture/design studio in Austin, TX. I encourage you to check out our website at www.vorrelandesign.com to get a sense of our vibe and culture. The graphic may or may not include the subtext to each value depending on how difficult it is to incorporate the subtext into a great design.

```html
<!DOCTYPE html>
<html lang="en">
<head>
<meta charset="utf-8">
<title>Our Values – Vorrelan Studio</title>
<link href="https://fonts.googleapis.com/css2?family=Roboto+Condensed:wght@400;700&family=Open+Sans:wght@400&display=swap" rel="stylesheet">
<style>
  :root {
    --page-bg: #ececec;
    --green-top: #a2c63f;
    --green-mid: #80a93a;
    --green-bottom: #3f773b;
    --ink: #ffffff;
    --dot-tone: rgba(120, 150, 40, 0.55);
  }
  * { margin: 0; padding: 0; box-sizing: border-box; }
  html, body {
    width: 1200px; height: 1200px; overflow: hidden;
    background: var(--page-bg);
  }
  .poster {
    position: absolute; left: 200px; top: 40px;
    width: 800px; height: 1120px; overflow: hidden;
    background: linear-gradient(180deg, var(--green-top) 0%, var(--green-mid) 42%, var(--green-bottom) 100%);
    color: var(--ink);
    font-family: "Roboto Condensed", "Arial Narrow", sans-serif;
  }
  .halftone-wave {
    position: absolute; left: 0; top: 0; width: 800px; height: 520px;
    background:
      radial-gradient(ellipse 70% 55% at 85% 35%, var(--dot-tone), transparent 70%),
      radial-gradient(ellipse 60% 40% at 20% 10%, rgba(120,150,40,0.35), transparent 70%);
    opacity: 0.6;
  }
  .brand {
    position: absolute; left: 0; right: 0; top: 96px;
    display: flex; justify-content: center; align-items: center; gap: 14px;
  }
  .brand-mark { width: 34px; height: 34px; background: var(--ink); }
  .brand-name {
    font-weight: 700; font-size: 40px; line-height: 40px; letter-spacing: 1px;
  }
  .brand-tagline {
    position: absolute; left: 0; right: 0; top: 158px; text-align: center;
    font-weight: 700; font-size: 21px; line-height: 26px; letter-spacing: 3px;
  }
  .title-our {
    position: absolute; left: 70px; top: 432px;
    transform: rotate(-90deg); transform-origin: left top;
    font-weight: 400; font-size: 80px; line-height: 60px; letter-spacing: 1px;
  }
  .title-values {
    position: absolute; left: 150px; top: 270px;
    font-weight: 700; font-size: 172px; line-height: 200px; letter-spacing: -2px;
  }
  .value { position: absolute; width: 300px; }
  .value-icon { position: absolute; left: -82px; top: 0; width: 62px; height: 62px; }
  .value-kicker { font-size: 24px; line-height: 26px; font-weight: 400; }
  .value-name { font-size: 38px; line-height: 38px; font-weight: 700; margin-top: 2px; }
  .value-text {
    font-family: "Open Sans", Arial, sans-serif;
    font-size: 15.5px; line-height: 22.5px; margin-top: 14px; white-space: nowrap;
  }
  .value--learners { left: 154px; top: 550px; }
  .value--trust { left: 500px; top: 550px; }
  .value--trust .value-text { margin-top: 26px; }
  .value--positive { left: 154px; top: 764px; }
  .value--responsive { left: 500px; top: 764px; }
  .website {
    position: absolute; left: 0; right: 0; top: 1024px; text-align: center;
    font-weight: 700; font-size: 28px;
  }
</style>
</head>
<body>
  <main class="poster">
    <div class="halftone-wave" role="img" aria-label="Halftone dot wave pattern"></div>

    <div class="brand">
      <div class="brand-mark"></div>
      <div class="brand-name">VORRELAN STUDIO</div>
    </div>
    <div class="brand-tagline">COMMERCIAL INTERIORS.</div>

    <div class="title-our">OUR</div>
    <h1 class="title-values">VALUES</h1>

    <section class="value value--learners">
      <svg class="value-icon" viewBox="0 0 62 62" fill="none" stroke="#fff" stroke-width="2" stroke-linejoin="round">
        <path d="M4 50 V24 l27 6 27-6 v26 l-27 6z"/>
        <path d="M31 30 v26"/>
        <circle cx="31" cy="18" r="10"/>
        <path d="M31 2 v4 M18 7 l3 3 M44 7 l-3 3"/>
      </svg>
      <div class="value-kicker">WE ARE</div>
      <h2 class="value-name">LEARNERS</h2>
      <p class="value-text">we look for opportunities to<br>learn from every project and<br>interaction, and we share<br>what we learn with each<br>other.</p>
    </section>

    <section class="value value--trust">
      <svg class="value-icon" viewBox="0 0 62 62" fill="none" stroke="#fff" stroke-width="2" stroke-linejoin="round">
        <path d="M34 6 h16 l6 8 -14 16 -14-16z"/>
        <circle cx="26" cy="22" r="10"/>
        <path d="M22 32 l-6 14"/>
        <path d="M2 40 h10 v16 H2z M12 44 h14 l6 6 -6 6 H12"/>
      </svg>
      <div class="value-kicker">WE ARE</div>
      <h2 class="value-name">JUSTWORTHY</h2>
      <p class="value-text">we are our client's advocate<br>and trustworthy teammate.</p>
    </section>

    <section class="value value--positive">
      <svg class="value-icon" viewBox="0 0 62 62" fill="none" stroke="#fff" stroke-width="2" stroke-linejoin="round">
        <circle cx="28" cy="34" r="24"/>
        <path d="M22 30 l10-14 c3-4 8-2 6 4 l-3 8 h14 c4 0 5 6 1 7 c3 2 2 6-1 7 c2 2 0 6-3 6 H30 l-8-4z"/>
        <path d="M12 30 h10 v22 H12z"/>
      </svg>
      <div class="value-kicker">WE ARE</div>
      <h2 class="value-name">POSITIVE</h2>
      <p class="value-text">we look for the good, roll<br>with the punches, have a<br>sence of humor and<br>celebrate other.</p>
    </section>

    <section class="value value--responsive">
      <svg class="value-icon" viewBox="0 0 62 62" fill="none" stroke="#fff" stroke-width="2" stroke-linejoin="round">
        <path d="M10 6 h44 v30 H10z"/>
        <path d="M4 40 h30 v12 H4z M2 52 h34"/>
        <path d="M38 30 h14 v24 H38z"/>
        <path d="M26 12 l-8 10 M36 12 l-12 14"/>
      </svg>
      <div class="value-kicker">WE ARE</div>
      <h2 class="value-name">RESPONSIVE</h2>
      <p class="value-text">we respond to our clients<br>quickly and with enthusiasm as<br>engaged teammates who are<br>committed to partnering with<br>them inaccomplishing<br>their goals.</p>
    </section>

    <div class="website">www.vorrelandesign.com</div>
  </main>
</body>
</html>
```